Velorix Flyer

PROJECT: Digital Flyer for VeloRix

Format
1920 × 1080 px (landscape, optimized for presentations and email)
Deliverables
• PDF
• PNG

About VeloRix
VeloRix is a Dutch B2B software company providing a unified CRM and customer journey platform. We help businesses manage the entire customer lifecycle — from first contact to loyal customer — by centralizing all touchpoints in one system.
What sets us apart:
Extreme ease of use. The system is self-guiding, shows only what's relevant per employee, and requires virtually no training. All channels (email, phone, chat, in-store) come together in one place with automatic task distribution. Built-in AI functions as a smart digital colleague that continuously learns.
Target audience:
Directors and sales managers at B2B companies with multiple customer contact channels.

Goal:
We want to create a flyer that sets us apart from other CRM platform providers. Our aim is to achieve this through simplicity and a professional appearance. The design should reflect our core value: ease of use. The recipient should feel compelled to engage with us — not overwhelmed by information, but intrigued by clarity. Less is more.

Required Text Elements
Headline:
"CRM that adapts to how you work"
Subline:
"Discover how VeloRix simplifies your sales process"
Call-to-action:
"See it in action — book a call"
Contact details:
• hello@velorix.nl
• 023-5718469
• velorix.com

Required Visual Elements
• VeloRix logo (attached)

Design Style
• Modern / Minimalist
• Professional / Business
• Tech / Futuristic
• Clean with plenty of whitespace

Tone of voice:
Clear, positive and customer-focused. Practical and accessible business style aimed at communicating concrete value for users.

Design inspiration — please review these websites:
• orbantal.com
• ravelo.app
• quendo.com
• tirameld.com
• gonwisp.com
What We DON'T Want
• Bold / In-your-face
• Dense / Compact
• Trendy / Experimental
• Childlike / Cheerful
• Playful / Cartoonish
• Busy / Chaotic
Colors
Use the color palette from velorix.com (blues, whites, clean professional tones).
[Exact hex codes used for element on the website:
#344054;
#1a1b1f;
#0254ac
#002249;
#e5edf7;
background-color: #fff; ]
Competitors (for context only — do NOT copy)
• brinvolt.nl
• kelmarin.com
• dortavecrm.com
• wexalunda.com
Budget
$150
Deadline
January 26, 2026

```html
<!DOCTYPE html>
<html lang="en">
<head>
<meta charset="utf-8">
<title>VeloRix Flyer</title>
<link href="https://fonts.googleapis.com/css2?family=Poppins:wght@400;600;700&display=swap" rel="stylesheet">
<style>
  :root {
    --stage: #a7a7a7;
    --paper: #ffffff;
    --navy: #10214f;
    --sky-blue: #169ddb;
    --lavender: #dcdcf5;
    --blush: #f3dfe8;
    --peach: #fbe6dc;
  }
  * { margin: 0; padding: 0; box-sizing: border-box; }
  html, body {
    width: 1200px; height: 1200px; overflow: hidden;
    background: var(--stage);
    font-family: "Poppins", sans-serif;
  }
  .flyer {
    position: absolute; left: 119px; top: 330px;
    width: 962px; height: 541px;
    background: var(--paper);
    overflow: hidden;
  }
  .flyer-shapes { position: absolute; inset: 0; }
  .brand {
    position: absolute; left: 50px; top: 34px;
    display: flex; align-items: center; gap: 18px;
  }
  .brand-dot {
    width: 66px; height: 66px; border-radius: 50%;
    background: var(--navy);
  }
  .brand-name {
    font-weight: 600; font-size: 72px; line-height: 1;
    color: var(--navy); letter-spacing: -1px;
  }
  .headline {
    position: absolute; left: 49px; top: 150px;
    font-weight: 700; font-size: 58px; line-height: 64px;
    letter-spacing: -0.5px; color: var(--navy);
  }
  .headline .accent { display: block; color: var(--sky-blue); }
  .subline {
    position: absolute; left: 50px; top: 303px;
    font-weight: 400; font-size: 26px; line-height: 32px;
    color: var(--navy);
  }
  .cta {
    position: absolute; left: 50px; top: 399px;
    font-weight: 700; font-size: 27px; line-height: 40px;
    color: var(--paper);
  }
  .phone {
    position: absolute; left: 53px; top: 465px;
    display: flex; align-items: center; gap: 14px;
  }
  .phone-number {
    font-weight: 700; font-size: 55px; line-height: 1;
    color: var(--paper); letter-spacing: 0.5px;
  }
  .contact-list {
    position: absolute; left: 620px; top: 470px;
    list-style: none; color: var(--paper);
    font-size: 20px; line-height: 26px;
  }
  .contact-list li { display: flex; align-items: center; gap: 12px; }
</style>
</head>
<body>
  <main class="flyer">
    <svg class="flyer-shapes" width="962" height="541" viewBox="0 0 962 541">
      <defs>
        <linearGradient id="fade" x1="0" y1="0" x2="1" y2="0">
          <stop offset="0.5" stop-color="#ffffff"/>
          <stop offset="0.75" stop-color="#f6f1f7"/>
          <stop offset="1" stop-color="#efe6f1"/>
        </linearGradient>
        <linearGradient id="sky" x1="0" y1="0" x2="0" y2="1">
          <stop offset="0" stop-color="#dcdcf5"/>
          <stop offset="0.5" stop-color="#f0e2ec"/>
          <stop offset="1" stop-color="#fbe6dc"/>
        </linearGradient>
      </defs>
      <rect width="962" height="442" fill="url(#fade)"/>
      <g role="img" aria-label="Soft pastel sky backdrop in a large circle">
        <circle cx="863" cy="183" r="264" fill="url(#sky)" stroke="#e6dbe3" stroke-width="2"/>
        <circle cx="853" cy="183" r="148" fill="#f1eaf2" opacity="0.5"/>
      </g>
      <rect y="442" width="962" height="99" fill="var(--navy)"/>
      <path d="M780 442 Q900 438 962 418 V442 Z" fill="var(--navy)"/>
      <path d="M0 442 H496 C522 488 552 518 586 541 H0 Z" fill="var(--sky-blue)"/>
      <path d="M0 394 H466 Q477 394 481 403 L496 442 H0 Z" fill="var(--navy)"/>
    </svg>

    <div class="brand">
      <span class="brand-dot"></span>
      <span class="brand-name">VeloRix</span>
    </div>

    <h1 class="headline">CRM that adapts<span class="accent">to how you work</span></h1>
    <p class="subline">Discover how VeloRix simplifies<br>your sales process</p>
    <p class="cta">See it in action — book a call</p>

    <div class="phone">
      <svg width="44" height="44" viewBox="0 0 44 44" aria-hidden="true">
        <circle cx="22" cy="22" r="22" fill="var(--navy)"/>
        <path d="M15 11c1-1 2.5-1 3.3.2l2.3 3.4c.6 1 .4 2.2-.5 2.9l-1.4 1.1c1 2.6 3 4.8 5.6 6l1.2-1.3c.8-.9 2.1-1 3-.3l3.3 2.5c1 .8 1.1 2.3.1 3.3l-1.6 1.7c-1.5 1.5-3.8 1.8-5.7.8-5.1-2.7-9-6.8-11.4-12-.8-1.9-.4-4 1-5.4z" fill="var(--sky-blue)"/>
      </svg>
      <span class="phone-number">023-5718469</span>
    </div>

    <ul class="contact-list">
      <li>
        <svg width="18" height="14" viewBox="0 0 18 14" aria-hidden="true"><rect width="18" height="14" rx="1.5" fill="#fff"/><path d="M1 1.5 9 8l8-6.5" stroke="var(--navy)" stroke-width="1.6" fill="none"/></svg>
        hello@velorix.nl
      </li>
      <li>
        <svg width="18" height="18" viewBox="0 0 18 18" aria-hidden="true" fill="none" stroke="#fff" stroke-width="1.2"><circle cx="9" cy="9" r="8"/><ellipse cx="9" cy="9" rx="3.5" ry="8"/><path d="M1 9h16M2.5 5h13M2.5 13h13"/></svg>
        velorix.com
      </li>
    </ul>
  </main>
</body>
</html>
```